Music producer seeks album cover!

Hi there designers. I need a design for my new album - the CD cover, CD itself and the album artwork for Tunevale and other streaming sites. This is my 'Salt and Ember' album: it's about gender and sexuality, and not conforming to labels. Musically it combines the pink of disco with the purple of rock.

The front cover should only be visuals and 'rowena dask' in all lower case with no capitals, and no album title, just a design in Salt and Ember please. I'd like to see something very simple, bold and iconic. For inspiration, how about jellyfish, squid, orca or zebra? All in Salt and Ember of course :-) Or how about the male and female parts of a flower, stamen and pistil?

For the back cover, I have quite a bit of text, attached as a word file.

The CD artwork and album artwork for streaming sites should be versions of the front cover. I will attach a template for the print-ready artwork . The streaming artwork needs to be a perfect square JPG or PNG, at least 4000 x 4000 pixels. It doesn't need the artist name.

```html
<!DOCTYPE html>
<html lang="en">
<head>
<meta charset="utf-8">
<title>rowena dask – Salt and Ember</title>
<link rel="stylesheet" href="https://fonts.googleapis.com/css2?family=Indie+Flower&family=Lora:wght@500;700&family=Open+Sans:wght@400;700&display=swap">
<style>
  :root {
    --stage: #eae6ee;
    --back-top: #7b1a70;
    --back-mid: #4e2a9c;
    --back-bottom: #2a1f8c;
    --back-glow: rgba(200, 160, 235, 0.45);
    --ink-light: #ffffff;
    --paper: #ffffff;
    --name-pink: #c96aaa;
    --name-purple: #6b3a9c;
    --art-magenta: #e0258f;
    --art-pink: #f06ab8;
    --art-violet: #7a3fb0;
    --art-plum: #4b2a78;
  }
  * { box-sizing: border-box; margin: 0; padding: 0; }
  html, body { width: 1200px; height: 1168px; overflow: hidden; }
  body { background: var(--stage); position: relative; font-family: "Open Sans", sans-serif; }

  /* Back cover */
  .back-cover {
    position: absolute; left: 55px; top: 28px; width: 537px; height: 529px;
    color: var(--ink-light);
    background:
      radial-gradient(ellipse 260px 280px at 150px 230px, var(--back-glow), transparent 70%),
      radial-gradient(ellipse 300px 200px at 380px 460px, rgba(150,120,230,0.35), transparent 70%),
      linear-gradient(170deg, var(--back-top) 0%, var(--back-mid) 55%, var(--back-bottom) 100%);
    box-shadow: 0 3px 8px rgba(0,0,0,0.35);
  }
  .tracklist { position: absolute; left: 40px; top: 28px; list-style: none;
    font-family: "Indie Flower", cursive; font-size: 18px; line-height: 25.7px; letter-spacing: 0.8px; white-space: nowrap; }
  .label-mark { position: absolute; left: 36px; top: 380px; width: 170px; text-align: center; }
  .label-mark .label-name { display: flex; align-items: center; justify-content: center; gap: 6px;
    font-weight: 700; font-size: 16px; white-space: nowrap; }
  .label-mark .label-dot { width: 10px; height: 10px; border-radius: 50%; background: var(--ink-light); flex: none; }
  .label-mark .label-url { font-size: 9px; letter-spacing: 1.5px; margin-top: 3px; }
  .intro { position: absolute; left: 235px; top: 38px; width: 250px; font-size: 12.3px; line-height: 15px; }
  .credits { position: absolute; left: 233px; top: 127px; width: 295px; font-size: 9.6px; line-height: 11.7px; white-space: nowrap; }
  .credits h3 { font-size: 9.6px; font-weight: 700; margin-bottom: 12px; }
  .credits .row .role { margin-left: 20px; }
  .credits .row .cont { display: block; padding-left: 71px; }
  .mastering { position: absolute; left: 0; right: 0; top: 433px; text-align: center; font-size: 9.6px; }
  .thanks { position: absolute; left: 26px; right: 26px; top: 455px; text-align: center; font-size: 9.6px; line-height: 11.2px; }

  /* Front cover */
  .front-cover { position: absolute; left: 612px; top: 27px; width: 556px; height: 533px;
    background: var(--paper); overflow: hidden; box-shadow: 0 3px 8px rgba(0,0,0,0.3); }
  .artist-name { position: absolute; font-family: "Lora", serif; font-weight: 700; letter-spacing: 4px; white-space: nowrap; }
  .artist-name .first { color: var(--name-pink); }
  .artist-name .last { color: var(--name-purple); }
  .front-cover .artist-name { left: 128px; top: 114px; font-size: 23px; }
  .art-jellyfish { position: absolute;
    background: linear-gradient(180deg, var(--art-magenta) 0%, var(--art-pink) 25%, var(--art-violet) 60%, var(--art-magenta) 100%);
    border-radius: 50% 40% 30% 40% / 25% 20% 40% 40%; opacity: 0.9; }
  .art-flower { position: absolute;
    background: linear-gradient(35deg, var(--art-violet) 0%, var(--art-magenta) 45%, var(--art-pink) 70%, var(--art-plum) 100%);
    border-radius: 10% 60% 40% 20%; opacity: 0.85; }
  .front-cover .art-jellyfish { left: 262px; top: 0; width: 293px; height: 492px; }
  .front-cover .art-flower { left: 0; top: 211px; width: 267px; height: 254px; }

  /* Disc */
  .disc { position: absolute; left: 347px; top: 591px; width: 504px; height: 504px; border-radius: 50%;
    background: var(--paper); overflow: hidden; box-shadow: 0 3px 8px rgba(0,0,0,0.3); }
  .disc .artist-name { left: 96px; top: 98px; font-size: 21px; }
  .disc .art-jellyfish { left: 300px; top: 33px; width: 210px; height: 420px; }
  .disc .art-flower { left: 0; top: 197px; width: 210px; height: 235px; }
  .disc-hole { position: absolute; left: 216px; top: 216px; width: 72px; height: 72px; border-radius: 50%; background: var(--stage); }
</style>
</head>
<body>

<section class="back-cover">
  <ol class="tracklist">
    <li>marlow</li>
    <li>daisy fenwick</li>
    <li>velvet girl</li>
    <li>paris took my heart</li>
    <li>is it cos it's snowing?</li>
    <li>tarnwick</li>
    <li>hollin wood</li>
    <li>ghosts</li>
    <li>quiet promises</li>
    <li>so long lovely</li>
  </ol>

  <div class="label-mark">
    <div class="label-name"><span class="label-dot"></span>northwind tones</div>
    <div class="label-url">northwindtones.com</div>
  </div>

  <p class="intro">Rowena Dask's Salt and Ember album was written and produced by Rowena Dask; spoken word on 'marlow' written by Odell Farran; string arrangement for 'paris took my heart' written by Nils Caddow</p>

  <div class="credits">
    <h3>Featuring, in order of appearance:</h3>
    <div class="row">Odell Farran<span class="role">spoken word, track 1</span></div>
    <div class="row">Kit Marrow (via Studioreach)<span class="role">organ on track 1,</span><span class="cont">electric piano on track 8</span></div>
    <div class="row">Rowena Dask<span class="role">vocals, guitars, bass guitar, keyboards,</span><span class="cont">sampler</span></div>
    <div class="row">Ferris Vale (via Studioreach)<span class="role">drums, tracks 1 and 2</span></div>
    <div class="row">Corinne Ysolde Mavet<span class="role">saxophones, tracks 1, 3, 9</span></div>
    <div class="row">Hattie Crane<span class="role">vocals, track 2</span></div>
    <div class="row">Velvet Echo (via Studioreach)<span class="role">vocals, tracks 2, 4, 5, 6, 7, 8, 10</span></div>
    <div class="row">Ravi Osler<span class="role">organ, track 2</span></div>
    <div class="row">Jory Dask<span class="role">guitar solo, track 2</span></div>
    <div class="row">Quinn Harlow (via Studioreach)<span class="role">beat programming, track 3</span></div>
    <div class="row">Dario Pellini (via Studioreach)<span class="role">piano, track 4</span></div>
    <div class="row">Ines Rowe<span class="role">vocals, track 4</span></div>
    <div class="row">Tomás Reyna Ibarra<span class="role">violins, track 4</span></div>
    <div class="row">Sam Kettering (via Studioreach)<span class="role">cello, track 4</span></div>
    <div class="row">Leon Brask (via Studioreach)<span class="role">drums, tracks 4, 5, 6, 7, 8, 9, 10</span></div>
    <div class="row">Maud Ellery<span class="role">spoken word, tracks 5, 7, 10</span></div>
    <div class="row">Corin (via Studioreach)<span class="role">vocals, tracks 6 and 8</span></div>
    <div class="row">Felix Orme<span class="role">spoken word, track 7</span></div>
    <div class="row">Ashby Noon<span class="role">vocals, tracks 7 and 10</span></div>
    <div class="row">Wes Penrith<span class="role">vocals, track 9</span></div>
  </div>

  <p class="mastering">Mastered by Glen Harcourt at ORBIT</p>
  <p class="thanks">Huge thanks to the team at Studioreach, to all the amazing musicians who put their soul into this record, and to my family and friends who continue to inspire, support and encourage me in my music. Peace and love to the female and the male, the binary and the non-binary, the conformers and the non-conformers, the salt and the ember.<br>Rowena Dask, 2023</p>
</section>

<section class="front-cover">
  <div class="art-flower" role="img" aria-label="Illustration of lily stamens and pistil in pink and purple"></div>
  <div class="art-jellyfish" role="img" aria-label="Illustration of a pink and purple jellyfish with trailing tentacles"></div>
  <h1 class="artist-name"><span class="first">rowena</span> <span class="last">dask</span></h1>
</section>

<section class="disc">
  <div class="art-flower" role="img" aria-label="Illustration of lily stamens and pistil in pink and purple"></div>
  <div class="art-jellyfish" role="img" aria-label="Illustration of a pink and purple jellyfish with trailing tentacles"></div>
  <h2 class="artist-name"><span class="first">rowena</span> <span class="last">dask</span></h2>
  <div class="disc-hole"></div>
</section>

</body>
</html>
```